Business Card for Orvane Parts Wholesale supplier

Hi There! I need a new business card for our company. We are specialized in selling Orvane parts, mostly we sell new LCD screens for Telvox and Slatrons. I would like to see that back in the design.

You can find the colors and logo's on our website: www.dorvak-example.nl

Industry/Entity Type

Business

Contact Information for Business Card

My Details:
Lars Vintorp

Phone: 0031612873406
E-mail: Lars@dorvak-example.nl

Slogan: "Because Quality Matters"

Font styles to use
Sans Serif

Colors

Designer to choose colors to be used in the design.

Requirements
Must have
• A Black backside with the Dorvak logo on it. The front side should be clean with only my contact details.
• But I'm also open for something really different or awesome!
Nice to have
• Remember that we are in the parts & repairing industry, So i'll be handing those business cards mainly to repair companies. Maybe you can do something with that thought :)

```html
<!DOCTYPE html>
<html lang="en">
<head>
<meta charset="utf-8">
<title>Dorvak Business Card</title>
<link rel="stylesheet" href="https://fonts.googleapis.com/css2?family=Source+Sans+3:wght@400;600;700&display=swap">
<style>
  :root {
    --backdrop: #b3b3b3;
    --card-white: #ffffff;
    --card-black: #000000;
    --brand-orange: #f26a1b;
    --ink: #111111;
    --divider: #8a8a8a;
    --paper-text: #ffffff;
  }
  * { margin: 0; padding: 0; box-sizing: border-box; }
  html, body {
    width: 1200px; height: 900px; overflow: hidden;
    background: var(--backdrop);
    font-family: "Source Sans 3", sans-serif;
  }
  .canvas { position: relative; width: 1200px; height: 900px; }
  .card {
    position: absolute; top: 306px; width: 440px; height: 271px;
    border-radius: 12px;
    box-shadow: 3px 4px 6px rgba(0,0,0,0.35);
  }
  .card--front { left: 149px; background: var(--card-white); }
  .card--back { left: 608px; background: var(--card-black); }

  .brand-mark { position: absolute; display: flex; align-items: center; }
  .brand-mark__dot { border-radius: 50%; background: var(--brand-orange); }
  .brand-mark__name { font-weight: 700; line-height: 1; letter-spacing: 0.5px; }

  .card--front .brand-mark { left: 22px; top: 78px; flex-direction: column; width: 190px; }
  .card--front .brand-mark__dot { width: 52px; height: 52px; margin-bottom: 12px; }
  .card--front .brand-mark__name { font-size: 52px; color: var(--ink); }

  .divider { position: absolute; left: 233px; top: 79px; width: 1px; height: 112px; background: var(--divider); }

  .contact { position: absolute; left: 252px; top: 96px; }
  .contact__name { font-size: 16.5px; font-weight: 400; color: var(--brand-orange); letter-spacing: 0.6px; margin-bottom: 12px; }
  .contact__list { list-style: none; }
  .contact__item { display: flex; align-items: center; font-size: 12.5px; color: var(--ink); height: 16px; }
  .contact__icon { width: 9px; height: 9px; margin-right: 6px; fill: var(--brand-orange); }

  .slogan {
    position: absolute; left: 0; right: 0; top: 232px; text-align: center;
    font-size: 13.5px; color: var(--brand-orange); letter-spacing: 0.2px;
  }

  .card--back .brand-mark { left: 73px; top: 101px; }
  .card--back .brand-mark__dot { width: 64px; height: 64px; margin-right: 14px; }
  .card--back .brand-mark__name { font-size: 58px; color: var(--paper-text); }

  .tagline {
    position: absolute; left: 0; right: 0; top: 192px; text-align: center;
    color: var(--paper-text); font-size: 18.5px; line-height: 23px;
  }
  .tagline strong { font-weight: 700; }
</style>
</head>
<body>
<main class="canvas">
  <section class="card card--front" aria-label="Business card front">
    <div class="brand-mark">
      <span class="brand-mark__dot"></span>
      <span class="brand-mark__name">dorvak</span>
    </div>
    <div class="divider"></div>
    <div class="contact">
      <p class="contact__name">LARS VINTORP</p>
      <ul class="contact__list">
        <li class="contact__item">
          <svg class="contact__icon" viewBox="0 0 10 10"><path d="M2 0.5 L3.6 2.6 L2.8 3.6 Q4 6 6.4 7.2 L7.4 6.4 L9.5 8 L8.6 9.5 Q3.5 9 0.5 1.4 Z"/></svg>
          0031612873406
        </li>
        <li class="contact__item">
          <svg class="contact__icon" viewBox="0 0 10 10"><path d="M0.5 2 H9.5 V8 H0.5 Z M0.5 2 L5 5.5 L9.5 2" stroke="#fff" stroke-width="0.8"/></svg>
          Lars@dorvak-example.nl
        </li>
        <li class="contact__item">
          <svg class="contact__icon" viewBox="0 0 10 10"><circle cx="5" cy="5" r="4.5"/><path d="M0.5 5 H9.5 M5 0.5 Q2.5 5 5 9.5 M5 0.5 Q7.5 5 5 9.5" stroke="#fff" stroke-width="0.7" fill="none"/></svg>
          www.dorvak-example.nl
        </li>
      </ul>
    </div>
    <p class="slogan">BECAUSE QUALITY MATTERS</p>
  </section>

  <section class="card card--back" aria-label="Business card back">
    <div class="brand-mark">
      <span class="brand-mark__dot"></span>
      <span class="brand-mark__name">dorvak</span>
    </div>
    <p class="tagline">The highest quality<br><strong>OEM parts</strong></p>
  </section>
</main>
</body>
</html>
```